Web design for a crypto donation landing page for wildlife protection projects

We are developing the landing page for the presale of a web3 project, which will collect cryptos to send them to wildlife protection projects.
Here some website we like:
https://www.tinyshareforcanopy.fr/
https://vorlq.io/
https://www.bramwild.io/
please, use the wireframe to know what blocks we want but we accept different template.
If possible, do the design on figma. Use 1 or 2 fonts max. Used green, blue and white, no more. Make a consistent system design by using the same font size for H1, H2, H3... and the same colors everywhere.
Number of Pages Required
1 page
Look and feel
Each slider illustrates characteristics of the customer's brand and the style your logo design should communicate.

```html
<!DOCTYPE html>
<html lang="fr">
<head>
<meta charset="utf-8">
<title>VerdaNova – Presale</title>
<link href="https://fonts.googleapis.com/css2?family=Lexend:wght@400;500;600;700&family=Poppins:wght@400;500;600&display=swap" rel="stylesheet">
<style>
:root{
  --violet:#3b23a8;
  --violet-deep:#2b1a8f;
  --violet-soft:#5a3fc4;
  --green:#2e9e3b;
  --green-bright:#3fbf3a;
  --grey-bg:#f2f2f2;
  --ink:#1b1b1b;
  --muted:#555;
  --white:#fff;
}
*{margin:0;padding:0;box-sizing:border-box}
html,body{width:1200px;height:4858px;overflow:hidden}
body{font-family:"Poppins",sans-serif;color:var(--ink);background:var(--white);position:relative}
h1,h2,h3,.display{font-family:"Lexend",sans-serif}
.abs{position:absolute}
section{position:relative;width:1200px;overflow:hidden}

/* HERO */
.hero{height:683px;background:linear-gradient(135deg,#3a1f9e 0%,#3b2cb0 55%,#4430b8 100%);color:var(--white)}
.hero .blob{position:absolute;border-radius:50%;background:rgba(80,60,200,.45)}
.brand{font-family:"Lexend",sans-serif;font-weight:500}
.hero .brand{left:115px;top:76px;font-size:24px}
.menu{right:70px;top:42px;width:30px}
.menu span{display:block;height:3px;background:var(--white);margin-bottom:4px}
.hero h1{left:112px;top:175px;font-size:48px;line-height:58px;font-weight:600;letter-spacing:.5px}
.hero .lead{left:112px;top:314px;font-family:"Lexend",sans-serif;font-weight:600;font-size:15px;line-height:30px;width:460px}
.hero .copy{left:112px;top:382px;width:440px;font-size:14px;line-height:24px}
.made{left:108px;top:506px;display:flex;align-items:center;gap:28px;font-family:"Lexend",sans-serif}
.made b{font-size:19px;font-weight:600}
.made .partner{display:flex;align-items:center;gap:12px;font-size:16px}
.made .partner i{width:32px;height:32px;border-radius:50%;background:#111;display:block}
.coins{left:111px;top:571px;display:flex;gap:14px}
.coins i{width:54px;height:54px;border-radius:50%;display:block;border:3px solid rgba(255,255,255,.15)}

.presale{left:653px;top:119px;width:436px;height:498px;background:var(--white);border-radius:22px;color:var(--ink);text-align:center}
.presale h2{margin-top:32px;font-size:32px;font-weight:500;letter-spacing:1px}
.presale .sub{font-size:14px;margin-top:6px}
.count{position:absolute;top:130px;left:22px;display:flex;gap:8px}
.count div{width:88px;height:82px;border-radius:8px;box-shadow:0 2px 8px rgba(0,0,0,.12);padding-top:6px}
.count b{display:block;font-family:"Lexend",sans-serif;font-size:38px;font-weight:500;line-height:46px}
.count span{font-size:14px;color:var(--green)}
.bar{position:absolute;left:38px;top:249px;width:356px;height:25px;background:#e6e6e6;border-radius:3px}
.bar i{display:block;width:141px;height:100%;background:var(--green);border-radius:3px}
.goal{position:absolute;top:293px;width:100%;font-size:13px}
.pm{position:absolute;top:304px;font-size:18px;font-weight:600}
.slider{position:absolute;left:30px;top:336px;width:377px;height:6px;background:#ddd;border-radius:3px}
.slider i{display:block;width:170px;height:100%;background:var(--green-bright);border-radius:3px}
.slider b{position:absolute;left:160px;top:-12px;width:30px;height:30px;border-radius:50%;background:var(--white);box-shadow:0 1px 5px rgba(0,0,0,.25);font-size:13px;font-weight:500;line-height:30px}
.price{position:absolute;top:370px;width:100%;font-size:22px}
.btn{display:inline-block;background:var(--green);color:var(--white);font-size:14px;font-weight:500;border-radius:3px}
.presale .btn{position:absolute;left:168px;top:430px;width:100px;height:43px;line-height:43px}

/* HOW */
.how{height:619px}
.section-title{font-size:36px;font-weight:500;text-align:center;line-height:48px}
.how .section-title{position:absolute;top:58px;width:100%}
.step{position:absolute;top:194px;width:312px;text-align:center}
.step.featured{background:var(--white);box-shadow:0 6px 22px rgba(0,0,0,.12);border-radius:6px;height:331px;top:194px}
.step .ico{width:90px;height:86px;margin:18px auto 0;border-radius:20px}
.step h3{font-size:25px;font-weight:500;line-height:34px;margin-top:20px}
.step p{font-size:13px;line-height:25px;color:var(--muted);margin:16px auto 0;width:275px}

/* COMMUNITY */
.community{height:468px;background:var(--grey-bg)}
.community h2{position:absolute;left:110px;top:48px;font-size:34px;font-weight:500;line-height:47px}
.community .intro{position:absolute;left:110px;top:164px;font-family:"Lexend",sans-serif;font-size:22px;line-height:29px}
.community .lead{position:absolute;left:110px;top:244px;font-family:"Lexend",sans-serif;font-size:20px;font-weight:500}
.checks{position:absolute;left:110px;top:296px;list-style:none}
.checks li{font-size:15px;font-weight:500;line-height:34px;display:flex;align-items:center;gap:8px}
.checks svg{width:14px;height:14px}
.social-big{position:absolute;left:864px;display:flex;align-items:center;gap:16px;font-family:"Lexend",sans-serif;font-size:31px;font-weight:600}
.social-big i{width:62px;height:62px;border-radius:50%;display:block}

/* ROADMAP */
.roadmap{height:1456px}
.roadmap .section-title{position:absolute;top:92px;width:100%;font-size:42px}
.rm-box{position:absolute;left:102px;top:192px;width:977px;height:1223px;border-radius:42px;overflow:hidden;background:linear-gradient(180deg,#3c2bb0 0%,#3a22a8 60%,#4630bf 100%)}
.rm-arc{position:absolute;left:120px;top:-370px;width:720px;height:720px;border-radius:50%;background:radial-gradient(circle at 50% 40%,#2a9a3c 0%,#2b8f45 60%,#2a7d56 85%,#3a3db0 100%)}
.rm-blob{position:absolute;border-radius:50%;background:rgba(90,70,210,.55)}
.rm-line{position:absolute;left:0;top:634px;width:100%;height:3px;background:var(--green-bright)}
.rm-dot{position:absolute;top:624px;width:24px;height:24px;border-radius:50%;background:var(--green)}
.phase{position:absolute;width:240px;color:var(--white)}
.phase h3{font-size:28px;font-weight:500;margin-bottom:24px}
.phase p{font-size:13px;line-height:21px;margin-bottom:22px;color:#e8e6ff}
.rm-nav{position:absolute;left:463px;top:1010px;display:flex;gap:10px}
.rm-nav i{width:24px;height:24px;border-radius:50%;display:flex;align-items:center;justify-content:center;color:#fff;font-style:normal;font-size:12px}

/* FAQ */
.faq{height:661px}
.faq .section-title{position:absolute;top:98px;width:100%;font-size:42px}
.faq-list{position:absolute;left:236px;top:200px;width:755px;list-style:none}
.faq-list li{height:78px;border-bottom:1px solid #ddd;display:flex;align-items:center;justify-content:space-between;padding:0 30px;font-family:"Lexend",sans-serif;font-size:20px;font-weight:500}
.faq-list svg{width:14px;height:14px}

/* TEAM */
.team{height:500px;background:var(--violet)}
.team .glow-a{position:absolute;left:-120px;top:250px;width:380px;height:380px;border-radius:50%;background:radial-gradient(circle,rgba(63,191,58,.75),rgba(63,191,58,0) 70%)}
.team .glow-b{position:absolute;right:-120px;top:-140px;width:380px;height:380px;border-radius:50%;background:radial-gradient(circle,rgba(63,191,58,.75),rgba(63,191,58,0) 70%)}
.team .section-title{position:absolute;top:60px;width:100%;font-size:42px;color:var(--white)}
.member{position:absolute;top:147px;width:174px;height:240px;background:var(--white);text-align:center;border-radius:2px}
.member .photo{position:absolute;left:6px;top:-10px;width:156px;height:156px;border-radius:50%;background:linear-gradient(160deg,#d9c2a8,#8a6a55)}
.member h3{position:absolute;left:0;top:168px;width:100%;font-size:15px;font-weight:500;line-height:21px}
.member .role{position:absolute;left:0;width:100%;font-size:11px;color:var(--muted);line-height:14px}

/* FOOTER */
.footer{height:471px;text-align:center}
.footer .brand{position:absolute;left:0;top:150px;width:100%;font-size:44px}
.foot-nav{position:absolute;top:264px;width:100%;display:flex;justify-content:center;gap:42px;font-size:15px}
.copyright{position:absolute;top:327px;width:100%;font-size:13px}
.copyright a{color:var(--green)}
.foot-social{position:absolute;top:382px;width:100%;display:flex;justify-content:center;gap:30px;align-items:center}
.foot-social i{width:42px;height:42px;border-radius:50%;display:block}
.foot-social i.sm{width:14px;height:14px;border:2px solid var(--green);background:none}
</style>
</head>
<body>

<section class="hero">
  <div class="blob" style="left:-80px;top:420px;width:360px;height:360px"></div>
  <div class="blob" style="left:820px;top:-160px;width:420px;height:360px"></div>
  <div class="blob" style="left:900px;top:440px;width:380px;height:380px;background:rgba(95,75,215,.5)"></div>
  <div class="abs brand">VerdaNova</div>
  <div class="abs menu"><span></span><span></span><span></span></div>
  <h1 class="abs">PROTÉGEONS LA<br>NATURE ENSEMBLE</h1>
  <p class="abs lead">FAITES UN DON DE TOKENS ET AIDEZ À PROTÉGER<br>LA FAUNE ET FLORE.</p>
  <p class="abs copy">Notre plateforme vous permet d'ajouter des tokens de votre choix pour les donner à un projet de protection de la nature. Votre contribution aidera à financer des actions concrètes pour préserver l'environnement.</p>
  <div class="abs made"><b>Made With</b><span class="partner"><i></i>Hashvale</span></div>
  <div class="abs coins">
    <i style="background:#eaeaf5"></i><i style="background:#2f9e3b"></i><i style="background:#e84142"></i>
  </div>

  <div class="abs presale">
    <h2>PRESALE</h2>
    <p class="sub">Temps restant avant la fin</p>
    <div class="count">
      <div><b>28</b><span>jours</span></div>
      <div><b>5</b><span>Heures</span></div>
      <div><b>39</b><span>minutes</span></div>
      <div><b>8</b><span>Secondes</span></div>
    </div>
    <div class="bar"><i></i></div>
    <p class="goal">20% de l'objectif</p>
    <span class="pm" style="left:32px">-</span><span class="pm" style="right:32px">+</span>
    <div class="slider"><i></i><b>12</b></div>
    <p class="price">12 token = 30€</p>
    <span class="btn">Acheter</span>
  </div>
</section>

<section class="how">
  <h2 class="section-title">Comment protéger la nature avec<br>des tokens VerdaNova ?</h2>
  <div class="step" style="left:112px">
    <div class="ico" role="img" aria-label="Illustration d'un token vert" style="background:linear-gradient(135deg,#7ed957,#2e9e3b);border-radius:50%"></div>
    <h3>Achetez des tokens<br>VerdaNova</h3>
    <p>Les tokens sont des actifs numériques qui peuvent être utilisés pour financer des projets des associations.</p>
  </div>
  <div class="step featured" style="left:443px">
    <div class="ico" role="img" aria-label="Illustration d'une ampoule et d'engrenages" style="background:linear-gradient(135deg,#f7b733,#3fa9f5)"></div>
    <h3>Votez pour un projet</h3>
    <p>Vous pouvez voter pour un projet de votre choix. Les projets sont proposés par des associations et des ONG qui travaillent pour la protection de la nature.</p>
  </div>
  <div class="step" style="left:776px">
    <div class="ico" role="img" aria-label="Illustration d'un échange de tokens" style="background:linear-gradient(135deg,#3fa9f5,#f7b733)"></div>
    <h3>Lassociation choisit<br>reçoit largent</h3>
    <p>Le projet qui a reçu le plus de votes recevra les tokens. L'association pourra utiliser cet argent pour financer ses actions concrètes pour protéger la nature.</p>
  </div>
</section>

<section class="community">
  <h2>Rejoignez la communauté pour soutenir<br>la protection de la nature</h2>
  <p class="intro">La nature est en danger, nous devons agir ensemble.<br>Rejoignez la communauté pour soutenir la protection de la nature.</p>
  <p class="lead">En rejoignant la communauté, vous pourrez :</p>
  <ul class="checks">
    <li><svg viewBox="0 0 14 14"><circle cx="7" cy="7" r="7" fill="#2e9e3b"/><path d="M4 7.2l2 2 4-4" stroke="#fff" stroke-width="1.8" fill="none"/></svg>Suivre les projets des associations qui travaillent pour la protection de la nature.</li>
    <li><svg viewBox="0 0 14 14"><circle cx="7" cy="7" r="7" fill="#2e9e3b"/><path d="M4 7.2l2 2 4-4" stroke="#fff" stroke-width="1.8" fill="none"/></svg>Voter pour le projet de votre choix et aider à financer ses actions concrètes.</li>
    <li><svg viewBox="0 0 14 14"><circle cx="7" cy="7" r="7" fill="#2e9e3b"/><path d="M4 7.2l2 2 4-4" stroke="#fff" stroke-width="1.8" fill="none"/></svg>Être informé des dernières actualités sur la protection de la nature.</li>
  </ul>
  <div class="social-big" style="top:134px;color:#5865f2"><i style="background:#5865f2"></i>Chatverse</div>
  <div class="social-big" style="top:212px"><i style="background:#111"></i>Chirper</div>
</section>

<section class="roadmap">
  <h2 class="section-title">Road Map</h2>
  <div class="rm-box">
    <div class="rm-arc"></div>
    <div class="rm-blob" style="left:340px;top:1000px;width:760px;height:460px"></div>
    <div class="rm-blob" style="left:-160px;top:1060px;width:420px;height:300px;background:rgba(70,50,190,.5)"></div>
    <div class="rm-line"></div>
    <div class="rm-dot" style="left:60px"></div>
    <div class="rm-dot" style="left:258px"></div>
    <div class="rm-dot" style="left:463px"></div>
    <div class="rm-dot" style="left:660px"></div>
    <div class="rm-dot" style="left:848px"></div>

    <div class="phase" style="left:255px;top:448px">
      <h3>Q2 2024</h3>
      <p>Site internet &amp; réseaux sociaux</p>
      <p>Marketing &amp; Développement du<br>smart contract tesnet</p>
    </div>
    <div class="phase" style="left:658px;top:346px">
      <h3>Q4 2024</h3>
      <p>Site internet &amp; réseaux sociaux</p>
      <p>Marketing &amp; Développement du<br>smart contract tesnet</p>
      <p>Juridique et Pré vente n°1</p>
      <p>Développement du smart<br>contract tesnet</p>
    </div>
    <div class="phase" style="left:58px;top:686px">
      <h3>Q1 2024</h3>
      <p>Site internet &amp; réseaux sociaux</p>
      <p>Marketing &amp; Développement du<br>smart contract tesnet</p>
      <p>Juridique et Pré vente n°1</p>
      <p>Développement du smart<br>contract tesnet</p>
    </div>
    <div class="phase" style="left:460px;top:686px">
      <h3>Q3 2024</h3>
      <p>Site internet &amp; réseaux sociaux</p>
      <p>Marketing &amp; Développement du<br>smart contract tesnet</p>
      <p>Juridique et Pré vente n°1</p>
      <p>Développement du smart<br>contract tesnet</p>
    </div>
    <div class="phase" style="left:845px;top:686px">
      <h3>Q1 2025</h3>
      <p>Site internet &amp; réseaux sociaux</p>
      <p>Marketing &amp; Développement du<br>smart contract tesnet</p>
      <p>Juridique et Pré vente n°1</p>
      <p>Développement du smart<br>contract tesnet</p>
    </div>
    <div class="rm-nav"><i style="background:#5a3fc4">‹</i><i style="background:#2e9e3b">›</i></div>
  </div>
</section>

<section class="faq">
  <h2 class="section-title">Frequently Asked Questions</h2>
  <ul class="faq-list">
    <li>Question 1<svg viewBox="0 0 14 14"><path d="M3 5l4 4 4-4" stroke="#222" stroke-width="1.6" fill="none"/></svg></li>
    <li>Question 2<svg viewBox="0 0 14 14"><path d="M3 5l4 4 4-4" stroke="#222" stroke-width="1.6" fill="none"/></svg></li>
    <li>Question 3<svg viewBox="0 0 14 14"><path d="M3 5l4 4 4-4" stroke="#222" stroke-width="1.6" fill="none"/></svg></li>
    <li>Question 4<svg viewBox="0 0 14 14"><path d="M3 5l4 4 4-4" stroke="#222" stroke-width="1.6" fill="none"/></svg></li>
    <li>Question 5<svg viewBox="0 0 14 14"><path d="M3 5l4 4 4-4" stroke="#222" stroke-width="1.6" fill="none"/></svg></li>
  </ul>
</section>

<section class="team">
  <div class="glow-a"></div><div class="glow-b"></div>
  <h2 class="section-title">Our Team</h2>
  <div class="member" style="left:260px">
    <div class="photo" role="img" aria-label="Portrait du fondateur"></div>
    <h3>Marchetti<br>Julien</h3>
    <span class="role" style="top:214px">Fondateur</span>
  </div>
  <div class="member" style="left:500px">
    <div class="photo" role="img" aria-label="Portrait de la développeuse blockchain" style="background:linear-gradient(160deg,#c98a6a,#7a2a2a)"></div>
    <h3 style="top:178px">Lemoine Camille</h3>
    <span class="role" style="top:202px">Développeuse blockchain</span>
  </div>
  <div class="member" style="left:740px">
    <div class="photo" role="img" aria-label="Portrait de la développeuse front-end" style="background:linear-gradient(160deg,#f3e2c4,#d9b48a)"></div>
    <h3 style="top:178px">Rinaldi Sophie</h3>
    <span class="role" style="top:204px">Développeur front-end</span>
  </div>
</section>

<section class="footer">
  <div class="brand">VerdaNova</div>
  <nav class="foot-nav"><span>Home</span><span>Blog</span><span>Astrologer Psychics</span><span>Talk Time Purchase</span></nav>
  <p class="copyright">Copyright© 2024 <a>VerdaNova</a> | All Rights Reserved</p>
  <div class="foot-social">
    <i style="background:#2e9e3b"></i><i class="sm"></i><i class="sm"></i><i class="sm"></i>
  </div>
</section>

</body>
</html>
```